Sleek, Professional Business Card Design Needed

Business Cards - Logo Attached.

We are a solar consulting company. We are national and want our cards to represent the professional high quality products that we offer.

Industry/Entity Type

Business

Contact Information for Business Card

n/a

Requirements
Must have
• Design
• Name
• Position
• Number
• Email
• Address
Should not have
• Not be too crowded

```html
<!DOCTYPE html>
<html lang="en">
<head>
<meta charset="utf-8">
<title>Brightfield Energy – Stationery</title>
<link href="https://fonts.googleapis.com/css2?family=Open+Sans:wght@400;600;700&display=swap" rel="stylesheet">
<style>
:root{
  --bg:#eef0f2;
  --paper:#ffffff;
  --ink:#2b2b2b;
  --muted:#555b61;
  --blue:#1679bf;
  --blue-card:#176ea8;
  --green:#7bb933;
  --shadow:0 6px 18px rgba(0,0,0,.12);
}
*{box-sizing:border-box;margin:0;padding:0}
html,body{width:1200px;height:800px;overflow:hidden}
body{background:var(--bg);font-family:'Open Sans',Arial,sans-serif;color:var(--ink);position:relative}

/* Letterhead */
.letterhead{position:absolute;left:70px;top:60px;width:480px;height:680px;background:var(--paper);box-shadow:var(--shadow);padding:44px 46px 0}
.brand{display:flex;align-items:center;gap:8px}
.brand-dot{width:26px;height:26px;border-radius:50%;background:var(--blue)}
.brand-name{font-weight:700;font-size:15px;color:var(--blue);letter-spacing:.3px}
.letterhead .brand{position:absolute;left:46px;top:44px}
.sender{position:absolute;right:46px;top:44px;font-size:7px;line-height:1.55;color:var(--muted);text-align:left}
.sender b{font-weight:600}
.recipient{margin-top:70px;font-size:8.5px;line-height:1.45}
.letter-body{margin-top:16px;font-size:8.5px;line-height:1.5;color:var(--ink)}
.letter-body p{margin-bottom:11px}
.signature{width:110px;height:32px;background:linear-gradient(90deg,#e9ebee,#f4f5f6);margin:6px 0 3px;border-radius:2px}
.sign-title{font-size:8.5px}
.letter-bands{position:absolute;left:0;right:0;bottom:30px;height:5px;display:flex}
.band-blue{flex:0 0 76%;background:var(--blue)}
.band-green{flex:1;background:var(--green)}

/* Cards */
.card{position:absolute;width:420px;height:240px;box-shadow:var(--shadow);overflow:hidden}
.card-front{left:640px;top:110px;background:var(--blue-card)}
.card-front .mark-faint{position:absolute;right:60px;top:-30px;width:190px;height:190px;border-radius:50%;border:14px solid rgba(255,255,255,.08)}
.card-front .brand{position:absolute;left:34px;bottom:46px}
.card-front .brand-name{color:#fff;font-size:19px}
.card-front .rule{position:absolute;left:34px;bottom:38px;width:190px;height:1px;background:var(--green)}

.card-back{left:640px;top:420px;background:var(--paper)}
.card-back .brand{position:absolute;left:30px;top:34px}
.person{position:absolute;left:30px;top:150px}
.person-name{font-size:13px;font-weight:700;letter-spacing:.4px}
.person-role{font-size:7.5px;color:var(--muted);letter-spacing:.6px;text-transform:uppercase;margin-top:2px}
.contacts{position:absolute;left:245px;top:38px;padding-left:14px;border-left:1px solid #c8ccd0;list-style:none;font-size:8px;line-height:1;color:var(--muted)}
.contacts li{display:flex;align-items:center;gap:7px;margin:7px 0}
.contacts svg{width:9px;height:9px;fill:var(--green);flex:none}
.card-bands{position:absolute;left:0;right:0;bottom:22px;height:4px;display:flex}
</style>
</head>
<body>

<section class="letterhead">
  <div class="brand"><span class="brand-dot"></span><span class="brand-name">BRIGHTFIELD ENERGY</span></div>
  <address class="sender">
    <b>PO Box 2210, Eastfield,<br>Westport 3307</b><br>
    e. office@brightfield.example<br>
    t. (04) 555 0142<br>
    f. (04) 555 0143
  </address>

  <div class="recipient">
    November 1, 2015<br>
    Mr. Alan Porter<br>
    58 Harbour Row<br>
    Norwick, U.K 40512
  </div>

  <div class="letter-body">
    <p>Dear Mr. Porter<br>
    The first paragraph of a typical business letter is used to state the main point of the letter. Begin with a friendly opening, then quickly transition into the purpose of your letter. Use a couple of sentences to explain the purpose, but do not go in to detail until the next paragraph.</p>
    <p>Beginning with the second paragraph, state the supporting details to justify your purpose. These may take the form of background information, statistics or first-hand accounts. A few short paragraphs within the body of the letter should be enough to support your reasoning. Finally, in the closing paragraph, briefly restate your purpose and why it is important. If the purpose of your letter is related to your employment, consider ending your letter with your contact information and title if it not included on letterhead.</p>
    <p>Finally, in the closing paragraph, briefly restate your purpose and why it is important. If the purpose of your letter is related to your employment, consider ending your letter with your contact information and title if it not included on letterhead. Finally, in the closing paragraph, briefly restate your purpose and why it is important. If the purpose of your letter is related to your employment, consider ending your letter with your contact information and title if it not included on letterhead.</p>
    <p>Finally, in the closing paragraph, briefly restate your purpose and why it is important. If the purpose of your letter is related to your employment, consider ending your letter with your contact information and title if it not included on letterhead. However, if the purpose is informational, think about closing with gratitude for the reader's time.</p>
    <p>Sincerely,</p>
    <div class="signature" role="img" aria-label="Handwritten signature of Martin Hale"></div>
    <div class="sign-title">President</div>
  </div>

  <div class="letter-bands"><span class="band-blue"></span><span class="band-green"></span></div>
</section>

<section class="card card-front">
  <span class="mark-faint"></span>
  <div class="brand"><span class="brand-name">BRIGHTFIELD ENERGY</span></div>
  <span class="rule"></span>
</section>

<section class="card card-back">
  <div class="brand"><span class="brand-dot"></span><span class="brand-name">BRIGHTFIELD ENERGY</span></div>
  <div class="person">
    <div class="person-name">DANIEL REEVE</div>
    <div class="person-role">Managing Director</div>
  </div>
  <ul class="contacts">
    <li><svg viewBox="0 0 10 10"><path d="M2 1h2l1 2-1 1a5 5 0 0 0 2 2l1-1 2 1v2c0 1-1 1-1 1A8 8 0 0 1 1 2s0-1 1-1z"/></svg>(04) 555 0187</li>
    <li><svg viewBox="0 0 10 10"><path d="M2 1h2l1 2-1 1a5 5 0 0 0 2 2l1-1 2 1v2c0 1-1 1-1 1A8 8 0 0 1 1 2s0-1 1-1z"/></svg>0400 555 201</li>
    <li><svg viewBox="0 0 10 10"><path d="M1 2h8v6H1z M1 2l4 3 4-3" stroke="#fff" stroke-width=".6"/></svg>daniel@brightfield.example</li>
    <li><svg viewBox="0 0 10 10"><circle cx="5" cy="5" r="4"/></svg>www.brightfield.example</li>
  </ul>
  <div class="card-bands"><span class="band-blue"></span><span class="band-green"></span></div>
</section>

</body>
</html>
```